Letterhead for invoices and engagement letter

Want to use logos sourced on quillorbit to create letterhead templates for word or pdf files

Industry/Entity Type

Legal- law firm

Colors
0054AA
0677BA
7BADD7
CADEEF
E8F1F8

```html
<!DOCTYPE html>
<html lang="en">
<head>
<meta charset="utf-8">
<title>The Harlow Firm – Letterhead</title>
<link rel="stylesheet" href="https://fonts.googleapis.com/css2?family=Roboto:wght@400;700&family=Roboto+Condensed:wght@400;700&family=Great+Vibes&display=swap">
<style>
  :root {
    --navy: #0a1f38;
    --ink: #111111;
    --paper: #ffffff;
    --footer-text: #ffffff;
  }
  * { margin: 0; padding: 0; box-sizing: border-box; }
  html, body { width: 941px; height: 1200px; overflow: hidden; background: var(--paper); }
  .letterhead {
    position: relative;
    width: 941px;
    height: 1200px;
    background: var(--paper);
    font-family: "Roboto", Arial, sans-serif;
    color: var(--ink);
  }
  .brand {
    position: absolute;
    left: 114px;
    top: 54px;
    display: flex;
    align-items: center;
    gap: 16px;
  }
  .brand-mark {
    width: 104px;
    height: 104px;
    border: 4px solid var(--navy);
    border-radius: 50%;
  }
  .brand-name {
    font-family: "Roboto", Arial, sans-serif;
    font-weight: 400;
    font-size: 30px;
    line-height: 34px;
    letter-spacing: 1.5px;
    color: var(--navy);
  }
  .sender {
    position: absolute;
    left: 114px;
    top: 234px;
    font-size: 16px;
    line-height: 20.6px;
  }
  .sender-name { font-weight: 700; font-size: 19px; line-height: 22px; }
  .sender-contact { margin-top: 10px; }
  .date-block {
    position: absolute;
    right: 93px;
    top: 234px;
    text-align: right;
    font-size: 16px;
    line-height: 20.6px;
  }
  .date-label { font-size: 19px; line-height: 22px; }
  .letter-body {
    position: absolute;
    left: 114px;
    top: 405px;
    width: 735px;
    font-size: 16px;
    line-height: 20.6px;
  }
  .salutation { margin-bottom: 20px; }
  .letter-body p.para { text-align: justify; margin-bottom: 20.6px; }
  .closing { margin-top: 0; }
  .signature {
    font-family: "Great Vibes", cursive;
    font-size: 40px;
    line-height: 44px;
    margin-top: 14px;
    color: var(--ink);
  }
  .signer {
    font-family: "Roboto Condensed", Arial, sans-serif;
    margin-top: 6px;
  }
  .signer-name { font-weight: 700; font-size: 19px; line-height: 21px; color: var(--navy); }
  .signer-role { font-size: 16px; line-height: 19px; }
  .footer-band {
    position: absolute;
    left: 0;
    top: 1081px;
    width: 941px;
    height: 95px;
    background: var(--navy);
    color: var(--footer-text);
  }
  .footer-contact {
    position: absolute;
    left: 135px;
    top: 20px;
    list-style: none;
    font-size: 14.5px;
    line-height: 19.5px;
    font-weight: 400;
  }
  .footer-contact li { display: flex; align-items: center; gap: 8px; }
  .footer-contact svg { width: 13px; height: 13px; fill: var(--footer-text); }
  .footer-address {
    position: absolute;
    right: 93px;
    top: 21px;
    text-align: right;
    font-size: 16px;
    line-height: 21px;
  }
</style>
</head>
<body>
<main class="letterhead">
  <header class="brand">
    <div class="brand-mark"></div>
    <div class="brand-name">THE<br>HARLOW<br>FIRM</div>
  </header>

  <section class="sender">
    <div class="sender-name">Name</div>
    <div>Owner</div>
    <div class="sender-contact">
      000-000-0000<br>
      some @some.com<br>
      Some street, Some city<br>
      Some country
    </div>
  </section>

  <section class="date-block">
    <div class="date-label">Date</div>
    <div>31 December 2024</div>
  </section>

  <article class="letter-body">
    <p class="salutation">Dear Mr. Name</p>
    <p class="para">Lorem ipsum dolor sit amet, consectetuer adipiscing elit, sed diam nonummy nibh euismod tincidunt ut laoreet dolore magna aliquam erat volutpat. Ut wisi enim ad minim veniam, quis nostrud exerci tation ullamcorper suscipit lobortis nisl ut aliquip ex ea commodo consequat. Duis autem vel eum iriure dolor in hendrerit in vulputate velit esse molestie.</p>
    <p class="para">Lorem ipsum dolor sit amet, cons ectetuer adipiscing elit, sed diam nonummy nibh euismod tincidunt ut laoreet dolore magna aliquam erat volutpat. Ut wisi enim ad minim veniam, quis nostrud exerci tation ullamcorper suscipit lobortis nisl ut aliquip ex ea commodo consequat.</p>
    <p class="para">Lorem ipsum dolor sit amet, consectetuer adipiscing elit, sed diam nonummy nibh euismod tincidunt ut laoreet dolore magna aliquam erat volutpat. Ut wisi enim ad minim veniam, quis nostrud exerci tation ullamcorper suscipit lobortis nisl ut aliquip ex ea commodo consequat.</p>
    <p class="closing">Thank you.</p>
    <div class="signature">Signature</div>
    <div class="signer">
      <div class="signer-name">Name</div>
      <div class="signer-role">Owner</div>
    </div>
  </article>

  <footer class="footer-band">
    <ul class="footer-contact">
      <li>
        <svg viewBox="0 0 24 24" aria-hidden="true"><path d="M6.6 10.8a15.1 15.1 0 0 0 6.6 6.6l2.2-2.2a1 1 0 0 1 1-.25 11.4 11.4 0 0 0 3.6.57 1 1 0 0 1 1 1V20a1 1 0 0 1-1 1A17 17 0 0 1 3 4a1 1 0 0 1 1-1h3.5a1 1 0 0 1 1 1c0 1.25.2 2.45.57 3.57a1 1 0 0 1-.25 1z"/></svg>
        000-000-0030
      </li>
      <li>
        <svg viewBox="0 0 24 24" aria-hidden="true"><path d="M2 5h20v2l-10 6L2 7z M2 9l10 6 10-6v10H2z"/></svg>
        info@theharlowfirm.com
      </li>
      <li>
        <svg viewBox="0 0 24 24" aria-hidden="true"><path d="M12 2a10 10 0 1 0 0 20 10 10 0 0 0 0-20zm0 2c.9 0 2.2 1.9 2.7 5H9.3C9.8 5.9 11.1 4 12 4zM4.3 11h3a16 16 0 0 0 0 2h-3a8 8 0 0 1 0-2zm5 0h5.4a14 14 0 0 1 0 2H9.3a14 14 0 0 1 0-2zm7.4 0h3a8 8 0 0 1 0 2h-3a16 16 0 0 0 0-2zM9.3 15h5.4c-.5 3.1-1.8 5-2.7 5s-2.2-1.9-2.7-5z"/></svg>
        www.theharlowfirm.com
      </li>
    </ul>
    <div class="footer-address">Address, Street, City,<br>Country Zip code</div>
  </footer>
</main>
</body>
</html>
```